Astrophotography equipment infographic

Hi! We need an infographic that displays different equipment used for astrophotography. Please see attached for further details.

```html
<!DOCTYPE html>
<html lang="en">
<head>
<meta charset="utf-8">
<title>Astrophotography Equipment</title>
<link rel="stylesheet" href="https://fonts.googleapis.com/css2?family=Exo+2:wght@300;400&display=swap">
<style>
  :root {
    --header-bg: #111923;
    --ink: #e8ebf0;
    --ink-soft: #c9ced6;
    --landscape-top: #1a2638;
    --landscape-mid: #2a3a55;
    --landscape-low: #131c2a;
    --solar-top: #060606;
    --solar-mid: #0b0b0b;
    --solar-glow: #b8440f;
    --solar-hot: #e6851f;
    --deep-top: #2a2522;
    --deep-mid: #5a3947;
    --deep-low: #4a3344;
  }
  * { box-sizing: border-box; margin: 0; padding: 0; }
  html, body { width: 800px; height: 1200px; overflow: hidden; background: #000; }
  body { font-family: "Exo 2", sans-serif; color: var(--ink); font-weight: 300; }
  .poster { position: relative; width: 800px; height: 1200px; overflow: hidden; }

  .header { position: absolute; left: 0; top: 0; width: 800px; height: 104px; background: var(--header-bg); }
  .header__icon { position: absolute; left: 8px; top: 10px; width: 64px; height: 66px; }
  .header__title { position: absolute; left: 100px; top: 12px; font-size: 44px; letter-spacing: 2px; font-weight: 300; line-height: 1; }
  .header__subtitle { position: absolute; left: 144px; top: 69px; font-size: 15px; letter-spacing: 0.6px; color: var(--ink-soft); line-height: 1; }

  .column { position: absolute; top: 104px; height: 1096px; }
  .column--landscape { left: 0; width: 274px;
    background: radial-gradient(ellipse at 75% 45%, var(--landscape-mid) 0%, transparent 60%),
                linear-gradient(180deg, var(--landscape-top), var(--landscape-low)); }
  .column--solar { left: 274px; width: 274px;
    background: linear-gradient(180deg, var(--solar-top) 0%, var(--solar-mid) 72%, var(--solar-glow) 90%, var(--solar-hot) 100%); }
  .column--deep { left: 548px; width: 252px;
    background: radial-gradient(ellipse at 50% 55%, var(--deep-mid) 0%, transparent 65%),
                linear-gradient(180deg, var(--deep-top) 0%, var(--deep-low) 60%, #3d2c3a 100%); }

  .item { position: absolute; left: 0; right: 0; text-align: center; line-height: 1; }
  .category { font-size: 24px; letter-spacing: 1px; }
  .label { font-size: 24px; letter-spacing: 1px; }
  .label--wide { font-size: 26px; }
  .note { font-size: 12px; line-height: 20px; color: var(--ink-soft); padding: 0 14px; }
  .note--small { font-size: 11px; line-height: 16px; }
  .note--tracker { font-size: 13px; line-height: 21.6px; }

  .scope { position: absolute; font-size: 13px; line-height: 22px; color: var(--ink-soft); }
  .icon { position: absolute; fill: none; stroke: var(--ink); stroke-width: 2; stroke-linecap: round; stroke-linejoin: round; }
  .icon .solid { fill: var(--ink); stroke: none; }
</style>
</head>
<body>
<main class="poster">

  <header class="header">
    <svg class="header__icon icon" viewBox="0 0 64 66" aria-hidden="true">
      <rect x="10" y="14" width="40" height="14" transform="rotate(-28 30 21)"/>
      <rect x="2" y="26" width="10" height="9" transform="rotate(-28 7 30)"/>
      <rect x="46" y="4" width="10" height="16" transform="rotate(-28 51 12)"/>
      <line x1="30" y1="32" x2="18" y2="64"/>
      <line x1="30" y1="32" x2="42" y2="64"/>
      <line x1="30" y1="32" x2="30" y2="62"/>
    </svg>
    <h1 class="header__title">Astrophotography Equipment</h1>
    <p class="header__subtitle">Typical equipment set-ups for different kinds of astrophotography</p>
  </header>

  <!-- Landscape -->
  <section class="column column--landscape" role="img" aria-label="Milky Way night sky over a dark landscape">
    <h2 class="item category" style="top:10px">[Landscape]</h2>
    <svg class="icon" style="left:22px;top:80px;width:62px;height:48px" viewBox="0 0 62 48" aria-hidden="true">
      <rect x="1" y="1" width="60" height="46"/><rect x="5" y="5" width="52" height="38"/>
      <circle cx="44" cy="15" r="4"/><path d="M5 40 L20 26 L30 34 L40 28 L57 40"/>
    </svg>
    <p class="scope" style="left:98px;top:77px">Capturing the Milky<br>Way above a landscape</p>

    <svg class="icon" style="left:48px;top:204px;width:74px;height:80px" viewBox="0 0 74 80" aria-hidden="true">
      <path d="M10 22 L58 14 Q70 14 72 28 L72 56 Q70 64 60 64 L18 68"/>
      <rect x="22" y="6" width="24" height="12"/>
      <circle cx="22" cy="56" r="20"/><circle cx="22" cy="56" r="13"/><circle cx="18" cy="52" r="3"/>
    </svg>
    <svg class="icon" style="left:142px;top:218px;width:92px;height:54px" viewBox="0 0 92 54" aria-hidden="true">
      <rect x="2" y="8" width="88" height="44" rx="3"/><rect x="14" y="2" width="18" height="6"/>
      <circle cx="60" cy="30" r="14"/><circle cx="60" cy="30" r="8"/><line x1="2" y1="16" x2="90" y2="16"/>
      <circle cx="82" cy="44" r="2"/>
    </svg>
    <h3 class="item label" style="top:302px">DSLR</h3>
    <p class="item note" style="top:333px">Camera with a full-frame sensor is best,<br>but not required.</p>

    <svg class="icon" style="left:96px;top:380px;width:76px;height:76px" viewBox="0 0 76 76" aria-hidden="true">
      <circle cx="38" cy="38" r="36"/>
      <path d="M24 12 L52 40 M60 22 L30 48 M62 50 L24 44 M42 66 L30 30 M14 54 L40 18 M16 26 L52 62"/>
    </svg>
    <h3 class="item label" style="top:473px">Wide Angle Lens</h3>
    <p class="item note note--small" style="top:509px">35mm for a full-frame camera, 24mm<br>or below for an APS-C sensor camera</p>

    <svg class="icon" style="left:106px;top:556px;width:60px;height:92px" viewBox="0 0 60 92" aria-hidden="true">
      <rect x="4" y="12" width="30" height="20"/><rect x="34" y="10" width="22" height="24"/><rect x="30" y="2" width="14" height="8"/>
      <line x1="20" y1="34" x2="4" y2="90"/><line x1="20" y1="34" x2="36" y2="90"/><line x1="20" y1="34" x2="20" y2="88"/>
    </svg>
    <h3 class="item label" style="top:666px">Tripod</h3>
    <h3 class="item label" style="top:700px">Sturdier the better</h3>

    <svg class="icon" style="left:98px;top:764px;width:70px;height:70px" viewBox="0 0 70 70" aria-hidden="true">
      <circle cx="35" cy="35" r="33"/><circle cx="35" cy="35" r="24"/><circle cx="35" cy="35" r="13"/><circle cx="35" cy="35" r="5"/>
      <path d="M38 18 L46 20 L42 26"/>
    </svg>
    <h3 class="item label" style="top:854px">Star Tracker</h3>
    <p class="item note note--tracker" style="top:888px">These sit between a camera and<br>tripod and move the camera with<br>the rotation of the earth, allowing<br>longer exposures without star trails<br>appearing.<br>(It's optional)</p>
  </section>

  <!-- Solar System -->
  <section class="column column--solar" role="img" aria-label="Planets, Moon and the surface of the Sun on a black background">
    <h2 class="item category" style="top:14px">[Solar System]</h2>
    <svg class="icon" style="left:14px;top:77px;width:62px;height:48px" viewBox="0 0 62 48" aria-hidden="true">
      <rect x="1" y="1" width="60" height="46"/><rect x="5" y="5" width="52" height="38"/>
      <circle cx="44" cy="15" r="4"/><path d="M5 40 L20 26 L30 34 L40 28 L57 40"/>
    </svg>
    <p class="scope" style="left:94px;top:78px">Capturing Sun, Moon,<br>Saturn, Jupiter and Other<br>Planets</p>

    <svg class="icon" style="left:36px;top:208px;width:74px;height:80px" viewBox="0 0 74 80" aria-hidden="true">
      <path d="M10 22 L58 14 Q70 14 72 28 L72 56 Q70 64 60 64 L18 68"/>
      <rect x="22" y="6" width="24" height="12"/>
      <circle cx="22" cy="56" r="20"/><circle cx="22" cy="56" r="13"/><circle cx="18" cy="52" r="3"/>
    </svg>
    <svg class="icon" style="left:128px;top:220px;width:92px;height:54px" viewBox="0 0 92 54" aria-hidden="true">
      <rect x="2" y="8" width="88" height="44" rx="3"/><rect x="14" y="2" width="18" height="6"/>
      <circle cx="60" cy="30" r="14"/><circle cx="60" cy="30" r="8"/><line x1="2" y1="16" x2="90" y2="16"/>
      <circle cx="82" cy="44" r="2"/>
    </svg>
    <h3 class="item label" style="top:304px;padding-right:32px">DSLR</h3>

    <svg class="icon" style="left:90px;top:388px;width:78px;height:48px" viewBox="0 0 78 48" aria-hidden="true">
      <rect x="2" y="4" width="74" height="40" rx="3"/>
      <path d="M10 6 V42 M16 6 V42 M22 6 V42 M28 6 V42 M34 6 V42"/>
      <rect x="44" y="10" width="14" height="28"/><rect x="48" y="14" width="6" height="10"/>
      <path d="M62 6 V42 M68 6 V42"/>
    </svg>
    <h3 class="item label" style="top:474px;padding-right:16px">Telephoto Lens</h3>
    <h3 class="item label" style="top:509px;padding-right:16px">85mm to 300mm</h3>

    <svg class="icon" style="left:100px;top:560px;width:60px;height:92px" viewBox="0 0 60 92" aria-hidden="true">
      <rect x="4" y="12" width="30" height="20"/><rect x="34" y="10" width="22" height="24"/><rect x="30" y="2" width="14" height="8"/>
      <line x1="20" y1="34" x2="4" y2="90"/><line x1="20" y1="34" x2="36" y2="90"/><line x1="20" y1="34" x2="20" y2="88"/>
    </svg>
    <h3 class="item label" style="top:670px;padding-right:16px">Tripod</h3>
    <h3 class="item label" style="top:702px;padding-right:16px">Sturdier the better</h3>

    <svg class="icon" style="left:96px;top:764px;width:70px;height:70px" viewBox="0 0 70 70" aria-hidden="true">
      <circle cx="35" cy="35" r="33"/><circle cx="35" cy="35" r="24"/><circle cx="35" cy="35" r="13"/><circle cx="35" cy="35" r="5"/>
      <path d="M38 18 L46 20 L42 26"/>
    </svg>
    <h3 class="item label" style="top:856px;padding-right:12px">Star Tracker</h3>
    <h3 class="item label" style="top:888px;padding-right:12px">It's optional</h3>
  </section>

  <!-- Deep Sky -->
  <section class="column column--deep" role="img" aria-label="Star field fading into a pink and purple nebula">
    <h2 class="item category" style="top:14px;padding-left:8px">[Deep Sky]</h2>
    <svg class="icon" style="left:10px;top:77px;width:62px;height:48px" viewBox="0 0 62 48" aria-hidden="true">
      <rect x="1" y="1" width="60" height="46"/><rect x="5" y="5" width="52" height="38"/>
      <circle cx="44" cy="15" r="4"/><path d="M5 40 L20 26 L30 34 L40 28 L57 40"/>
    </svg>
    <p class="scope" style="left:90px;top:82px;line-height:24px">Capturing Galaxies,<br>Nebulae etc</p>

    <svg class="icon" style="left:96px;top:196px;width:64px;height:76px" viewBox="0 0 64 76" aria-hidden="true">
      <rect x="14" y="14" width="44" height="14" transform="rotate(-28 36 21)"/>
      <rect x="2" y="28" width="12" height="10" transform="rotate(-28 8 33)"/>
      <line x1="34" y1="36" x2="20" y2="74"/><line x1="34" y1="36" x2="48" y2="74"/><line x1="34" y1="36" x2="34" y2="70"/>
    </svg>
    <h3 class="item label label--wide" style="top:301px;padding-left:8px">Specialist Camera</h3>
    <p class="item note" style="top:337px">Specialist astrophotography camera<br>(eg, CCD camera) or adapted DSLR<br>camera with IR filter</p>

    <svg class="icon" style="left:80px;top:472px;width:100px;height:112px" viewBox="0 0 100 112" aria-hidden="true">
      <rect x="24" y="14" width="64" height="22" rx="3" transform="rotate(-22 56 25)"/>
      <rect x="6" y="34" width="18" height="14" transform="rotate(-22 15 41)"/>
      <line x1="28" y1="14" x2="44" y2="6"/><circle cx="36" cy="46" r="6"/>
      <line x1="36" y1="52" x2="14" y2="110"/><line x1="36" y1="52" x2="58" y2="110"/><line x1="36" y1="52" x2="36" y2="104"/>
      <line x1="22" y1="84" x2="50" y2="84"/>
    </svg>
    <h3 class="item label" style="top:594px">Telescope</h3>
    <p class="item note" style="top:624px">Telescope with the camera attached<br>this works in place of a camera<br>lens</p>

    <svg class="icon" style="left:40px;top:720px;width:56px;height:90px" viewBox="0 0 60 92" aria-hidden="true">
      <rect x="4" y="12" width="30" height="20"/><rect x="34" y="10" width="22" height="24"/><rect x="30" y="2" width="14" height="8"/>
      <line x1="20" y1="34" x2="4" y2="90"/><line x1="20" y1="34" x2="36" y2="90"/><line x1="20" y1="34" x2="20" y2="88"/>
    </svg>
    <svg class="icon" style="left:142px;top:736px;width:54px;height:60px" viewBox="0 0 54 60" aria-hidden="true">
      <rect class="solid" x="0" y="0" width="54" height="18" rx="3"/>
      <rect class="solid" x="8" y="20" width="38" height="6"/>
      <path class="solid" d="M14 28 H40 V50 H32 V58 H22 V50 H14 Z"/>
      <circle cx="27" cy="39" r="5" fill="var(--deep-low)" stroke="none"/>
    </svg>
    <h3 class="item label" style="top:860px;padding-right:32px">Tripod, Telescope</h3>
    <h3 class="item label" style="top:898px;padding-right:32px">Mount</h3>
  </section>

</main>
</body>
</html>
```